Real Estate Agency Facebook Cover Photo

We need a Facebook cover photo created for our Real Estate Business. We also need this cover photo adapted to several other platforms. Please read this google doc for full specifications of the job https://papers.vellomarsh.com/sheet/d/8QwPzLk3RtYvB2nHs7JxVaM5_cEdGoUfNpLkZrWbYq/view?mode=shared

Please also carefully read the Must Haves/Should Not Haves

Please contact me if you have any queries. Looking forward to seeing your designs!

Doran

Industry/Entity Type

Real Estate Agent

Requirements
Must have
• The Taglines 'More Money In Your Pocket' and sub tagline 'With Our Low Flat Fee To Sell Your Home'

It can then also have other elements e.g our logo, contact details and anything else you think will work well.

It must also have great graphic design work which looks custom and very clean/modern
Should not have
• Must not have poor quality stock images or anything tacky regarding money etc

```html
<!DOCTYPE html>
<html lang="en">
<head>
<meta charset="utf-8">
<title>Kestro – Facebook Cover</title>
<link rel="stylesheet" href="https://fonts.googleapis.com/css2?family=Oswald:wght@600;700&family=Open+Sans:ital,wdth,wght@0,75..100,300..500;1,75..100,300..500&display=swap">
<style>
  :root {
    --page: #ffffff;
    --ink-black: #050505;
    --chevron-soft: #0e0e0e;
    --chevron-softer: #141414;
    --brand-red: #ec1c24;
    --red-deep: #8e0f14;
    --red-darker: #4a0a0c;
    --white: #ffffff;
    --photo-light: #eceef1;
    --photo-mid: #d9dde3;
    --photo-warm: #e9c9b8;
  }
  html, body {
    margin: 0;
    padding: 0;
    width: 1200px;
    height: 1200px;
    overflow: hidden;
    background: var(--page);
  }
  .cover {
    position: absolute;
    left: 103px;
    top: 411px;
    width: 994px;
    height: 378px;
    overflow: hidden;
    background: var(--ink-black);
  }
  .cover-art {
    position: absolute;
    inset: 0;
    width: 994px;
    height: 378px;
  }
  .cover-text {
    position: absolute;
    inset: 0;
    width: 994px;
    height: 378px;
  }
  .brand-name {
    font-family: "Open Sans", sans-serif;
    font-weight: 400;
    fill: var(--brand-red);
    letter-spacing: 4px;
  }
  .headline {
    font-family: "Oswald", sans-serif;
    font-weight: 700;
    fill: var(--brand-red);
  }
  .subline {
    font-family: "Open Sans", sans-serif;
    font-style: italic;
    font-weight: 300;
    font-stretch: 75%;
    fill: var(--white);
  }
  .phone-number {
    font-family: "Oswald", sans-serif;
    font-weight: 700;
    fill: var(--brand-red);
  }
  .contact-line {
    font-family: "Open Sans", sans-serif;
    font-weight: 400;
    font-stretch: 75%;
    fill: var(--white);
  }
</style>
</head>
<body>
  <section class="cover" aria-label="Kestro Facebook cover">
    <svg class="cover-art" viewBox="0 0 994 378" xmlns="http://www.w3.org/2000/svg">
      <defs>
        <linearGradient id="photoTone" x1="0" y1="0" x2="1" y2="1">
          <stop offset="0" stop-color="var(--photo-light)"/>
          <stop offset="0.45" stop-color="var(--photo-mid)"/>
          <stop offset="0.75" stop-color="var(--photo-light)"/>
          <stop offset="1" stop-color="var(--photo-warm)"/>
        </linearGradient>
      </defs>
      <rect class="photo-area" x="600" y="0" width="394" height="378" fill="url(#photoTone)" role="img" aria-label="Photo of colleagues' hands working over documents at a white desk"/>
      <polygon class="chevron-panel" points="0,0 642,0 748,182 642,378 0,378" fill="var(--ink-black)"/>
      <polygon class="chevron-shade" points="356,0 642,0 748,182 642,378 356,378 462,182" fill="var(--chevron-soft)"/>
      <polygon class="chevron-shade" points="452,0 642,0 748,182 642,378 452,378 558,182" fill="var(--chevron-softer)"/>
      <polygon class="chevron-shade" points="548,0 642,0 748,182 642,378 548,378 654,182" fill="#181818"/>
      <polygon class="corner-stripe" points="0,0 118,0 0,121" fill="var(--red-darker)"/>
      <polygon class="corner-stripe" points="0,0 96,0 0,98" fill="var(--red-deep)"/>
      <polygon class="corner-stripe" points="0,0 74,0 0,76" fill="#b8141a"/>
      <polygon class="corner-stripe" points="0,0 50,0 0,52" fill="var(--brand-red)"/>
      <g class="phone-icon" fill="none" stroke="var(--brand-red)" stroke-width="2.4" stroke-linecap="round" stroke-linejoin="round">
        <line x1="75" y1="280" x2="75" y2="285"/>
        <line x1="62" y1="284" x2="65" y2="288"/>
        <line x1="88" y1="284" x2="85" y2="288"/>
        <line x1="56" y1="294" x2="61" y2="294"/>
        <line x1="89" y1="294" x2="94" y2="294"/>
        <rect x="64" y="292" width="22" height="38" rx="3"/>
        <path d="M64 304 q-9 2 -8 10 q-3 6 2 11 q4 8 14 10 l6 10 l11 -8 l-8 -9 q2 -10 -6 -16"/>
      </g>
      <rect class="contact-divider" x="110" y="281" width="2" height="69" fill="var(--brand-red)"/>
    </svg>
    <svg class="cover-text" viewBox="0 0 994 378" xmlns="http://www.w3.org/2000/svg">
      <text class="brand-name" x="50" y="108" font-size="44" textLength="214" lengthAdjust="spacingAndGlyphs">KESTRO</text>
      <text class="headline" x="50" y="179" font-size="70" textLength="637" lengthAdjust="spacingAndGlyphs">MORE MONEY IN YOUR POCKET</text>
      <text class="subline" x="50" y="216" font-size="29" textLength="421" lengthAdjust="spacingAndGlyphs">With Our Low Flat Fee To Sell Your Home</text>
      <text class="phone-number" x="124" y="320" font-size="42" textLength="245" lengthAdjust="spacingAndGlyphs">+61 2 5550 1847</text>
      <text class="contact-line" x="124" y="343" font-size="16" textLength="245" lengthAdjust="spacingAndGlyphs">info@kestro.com  |  WWW.KESTRO.COM.AU</text>
    </svg>
  </section>
</body>
</html>
```